Talent Management Company Needs Business Cards

Using one of the logos provided (attached) K&R Talent Collective needs a business card designed.
Please visit our website for more information about us-

www.krtalentcollective.example

The face should feature a dramatic presentation of the logo with the back being reserved for our professional information which is:

The information should be:
Dorian T. Vickers
C.E.O
Email: dtvickers@krtalentcollective.example
Mobile: 555-804-2917
Website: www.krtalentcollective.example

Marcus L. Vickers
Director of Public Relations
Email: mlvickers@krtalentcollective.example
Mobile: 555-806-3350

Jules R. Hampton
Director of Client Development
Email: jhampton@krtalentcollective.example

Simon Hurlock
Director of Brand Development
Email: shurlock@krtalentcollective.example

Would like the logo to have color. I would like to see one side red or black and the other side white but if it looks better in either black or red that would be fine to but would like to see how it comes out.

Please feel free to message me and if you would like just the icon alone I have other image files that I can send as well.

Target Market(s)

Professional Athletes, coaches, entertainers age 18-35 but also must be accepted in the business community

Industry/Entity Type

Business

Requirements
Must have
• 1) Use the logo
2) Double sided
3) Distinctive
Nice to have
• Small simple images for telephone, e-mail, and Url.

```html
<!DOCTYPE html>
<html lang="en">
<head>
<meta charset="utf-8">
<title>K&amp;R Talent Collective — Business Card</title>
<link rel="stylesheet" href="https://fonts.googleapis.com/css2?family=Arimo:wght@400;700&display=swap">
<style>
  :root {
    --backdrop: #8e8d8a;
    --card-black: #141414;
    --card-black-edge: #1d1d1d;
    --red-bright: #d01a24;
    --red-mid: #a8121a;
    --red-deep: #6e0a0f;
    --red-accent: #c8161f;
    --silver: #d7d9dc;
    --text-light: #f2f2f2;
    --text-muted: #bdbdbd;
    --divider: #9a9a9a;
  }
  * { box-sizing: border-box; margin: 0; padding: 0; }
  html, body { width: 1200px; height: 792px; overflow: hidden; }
  body {
    background: var(--backdrop);
    font-family: "Arimo", Arial, sans-serif;
    position: relative;
  }
  .card {
    position: absolute;
    top: 241px;
    width: 540px;
    height: 309px;
    box-shadow: 0 10px 24px rgba(0,0,0,.35);
    overflow: hidden;
  }

  /* Contact side */
  .card--contact {
    left: 40px;
    background: linear-gradient(160deg, var(--card-black-edge), var(--card-black));
  }
  .brand-block {
    position: absolute;
    left: 0; top: 0;
    width: 236px; height: 100%;
    display: flex;
    align-items: center;
    justify-content: center;
  }
  .brand-lockup {
    display: flex;
    flex-direction: column;
    align-items: center;
    gap: 14px;
  }
  .brand-square {
    width: 40px; height: 40px;
    background: var(--red-accent);
    flex: none;
  }
  .brand-name {
    color: var(--text-light);
    font-weight: 400;
    font-size: 12px;
    letter-spacing: .06em;
    text-transform: uppercase;
    white-space: nowrap;
  }
  .divider {
    position: absolute;
    left: 236px; top: 58px;
    width: 1.5px; height: 200px;
    background: var(--divider);
  }
  .person {
    position: absolute;
    left: 262px; top: 64px;
    color: var(--text-light);
  }
  .person-name {
    font-weight: 700;
    font-size: 20px;
    letter-spacing: .01em;
  }
  .person-title {
    font-size: 11px;
    color: var(--text-muted);
    margin-top: 8px;
  }
  .contact-list {
    list-style: none;
    margin-top: 26px;
  }
  .contact-item {
    display: flex;
    align-items: center;
    gap: 10px;
    font-size: 11.5px;
    line-height: 1;
    margin-bottom: 11px;
    color: var(--text-light);
    white-space: nowrap;
  }
  .contact-icon {
    width: 13px; height: 13px;
    flex: none;
    fill: none;
    stroke: var(--text-light);
    stroke-width: 1.4;
  }

  /* Brand side */
  .card--brand {
    left: 620px;
    background: radial-gradient(ellipse at 30% 10%, var(--red-bright) 0%, var(--red-mid) 45%, var(--red-deep) 100%);
  }
  .brand-side-mark {
    position: absolute;
    left: 40px; top: 50%;
    transform: translateY(-50%);
    display: flex;
    align-items: center;
    gap: 26px;
  }
  .brand-side-mark .brand-square {
    width: 190px; height: 190px;
    background: linear-gradient(145deg, #eceef0, #a9acb0);
    box-shadow: 0 6px 18px rgba(0,0,0,.3);
  }
  .brand-side-mark .brand-name {
    font-size: 21px;
    letter-spacing: .05em;
    line-height: 1.35;
    white-space: normal;
    width: 250px;
  }
</style>
</head>
<body>
  <section class="card card--contact" aria-label="Contact side">
    <div class="brand-block">
      <div class="brand-lockup">
        <span class="brand-square"></span>
        <span class="brand-name">K&amp;R Talent Collective</span>
      </div>
    </div>
    <div class="divider"></div>
    <div class="person">
      <h1 class="person-name">Dorian T. Vickers</h1>
      <p class="person-title">C.E.O</p>
      <ul class="contact-list">
        <li class="contact-item">
          <svg class="contact-icon" viewBox="0 0 14 14"><rect x="3.5" y="0.8" width="7" height="12.4" rx="1.2"/><line x1="6" y1="11" x2="8" y2="11"/></svg>
          555-804-2917
        </li>
        <li class="contact-item">
          <svg class="contact-icon" viewBox="0 0 14 14"><circle cx="7" cy="7" r="2.4"/><path d="M9.4 7v1.2a1.8 1.8 0 0 0 3.6 0V7A6 6 0 1 0 10 12.2"/></svg>
          dtvickers@krtalentcollective.example
        </li>
        <li class="contact-item">
          <svg class="contact-icon" viewBox="0 0 14 14"><circle cx="7" cy="7" r="6"/><ellipse cx="7" cy="7" rx="2.6" ry="6"/><line x1="1" y1="7" x2="13" y2="7"/></svg>
          www.krtalentcollective.example
        </li>
      </ul>
    </div>
  </section>

  <section class="card card--brand" aria-label="Brand side">
    <div class="brand-side-mark">
      <span class="brand-square"></span>
      <span class="brand-name">K&amp;R Talent Collective</span>
    </div>
  </section>
</body>
</html>
```